Business Cards for new orthopaedic surgery practice

My husband and I are starting our own orthopaedic surgery practice. We are looking for a business card that is uniform, but one will have my name/title and the other will have his. You can just create one design with my name on it for now. But when I choose your design as the winning design I will ask that you add another copy with his name/title.

We are looking for classy, simple, elite all in one. We like dark blues/a little gold/yellow. Something that goes with our logo. We want our logo incorporated. Here is all the info you need:
Business name: RV Spine & Vitality Center
Location: 38157 North Harbor Blvd
Coral Springs, FL 33058
Phone: 954-218-4630
Fax: 954-581-2473
Email: info@myrvspine.example

Names: Lorena Vickers, M.D.
Board Certified Hand and Upper Extremity Surgeon

Eban Sorley, M.D.
Board Certified Hip & Knee Replacement/General Orthopaedic Surgeon

Can decide what you want to put on the back. Maybe a slogan:
Steady in Skill. Centered on You

I am just going to upload our logo. The only thing is if we select you as the winning design, the location, and phone numbers may change. We will need your help to update that once fully solidified.

Industry/Entity Type

Medical

Contact Information for Business Card

Colors
0054AA
0677BA
7BADD7
CADEEF
E8F1F8
0094D4
00A9DD
6FCCEA
C7EBF8
E9F6FB

Requirements
Must have
• class, appeal,
Should not have
• We want to air on the side of masculine if we are looking at masculine vs. feminine feel. But we still want it classy, sophisticated, and something we will love

```html
<!DOCTYPE html>
<html lang="en">
<head>
<meta charset="utf-8">
<title>RV Spine &amp; Vitality Center — Business Card</title>
<link href="https://fonts.googleapis.com/css2?family=Poppins:wght@400;500;600&display=swap" rel="stylesheet">
<style>
  :root {
    --navy: #283f8a;
    --cyan: #1fb3e0;
    --white: #ffffff;
    --ink: #4a4f5c;
    --page: #e6e9ef;
  }
  * { box-sizing: border-box; margin: 0; padding: 0; }
  html, body { width: 1200px; height: 900px; overflow: hidden; }
  body {
    background: var(--page);
    font-family: "Poppins", sans-serif;
    position: relative;
  }
  .card {
    position: absolute;
    left: 260px;
    width: 680px;
    height: 389px;
    background: var(--navy);
    overflow: hidden;
    box-shadow: 0 10px 30px rgba(20, 30, 70, .25);
  }
  .card--front { top: 36px; }
  .card--back { top: 470px; }

  /* brand lockup */
  .brand {
    position: absolute;
    display: flex;
    align-items: center;
    gap: 18px;
    color: var(--white);
  }
  .brand__dot {
    width: 26px; height: 26px;
    border-radius: 50%;
    background: var(--white);
    flex: none;
  }
  .brand__name {
    font-weight: 600;
    text-transform: uppercase;
    letter-spacing: 1.5px;
    line-height: 1.1;
    white-space: nowrap;
  }
  .card--front .brand { left: 170px; top: 108px; }
  .card--front .brand__name { font-size: 34px; }

  .tagline {
    position: absolute;
    left: 150px; right: 150px;
    top: 260px;
    padding: 10px 0;
    border-top: 1.5px solid var(--cyan);
    border-bottom: 1.5px solid var(--cyan);
    text-align: center;
    color: var(--white);
    font-size: 19px;
    letter-spacing: .5px;
    white-space: nowrap;
  }

  /* back side */
  .card--back .brand { left: 36px; top: 40px; }
  .card--back .brand__dot { width: 18px; height: 18px; }
  .card--back .brand__name { font-size: 22px; }

  .doctor {
    position: absolute;
    right: 48px; top: 150px;
    text-align: right;
  }
  .doctor__name {
    color: var(--cyan);
    font-weight: 600;
    font-size: 21px;
    letter-spacing: .5px;
  }
  .doctor__title {
    color: var(--white);
    font-size: 14px;
    margin-top: 2px;
  }
  .accent-bar {
    position: absolute;
    right: 0; top: 150px;
    width: 14px; height: 58px;
    background: var(--cyan);
  }

  .contact-panel {
    position: absolute;
    left: 0; bottom: 0;
    width: 62%;
    height: 48%;
    background: var(--white);
    padding: 22px 36px;
    color: var(--ink);
    font-size: 14px;
    line-height: 1.5;
  }
  .contact-panel address { font-style: normal; margin-bottom: 6px; }
  .contact-line { display: flex; align-items: center; gap: 8px; }
  .contact-line svg { width: 13px; height: 13px; flex: none; }
</style>
</head>
<body>

  <section class="card card--front" aria-label="Card front">
    <div class="brand">
      <span class="brand__dot"></span>
      <div class="brand__name">RV Spine &amp;<br>Vitality Center</div>
    </div>
    <p class="tagline">Steady in Skill. Centered on You</p>
  </section>

  <section class="card card--back" aria-label="Card back">
    <div class="brand">
      <span class="brand__dot"></span>
      <div class="brand__name">RV Spine &amp;<br>Vitality Center</div>
    </div>

    <div class="doctor">
      <p class="doctor__name">Lorena Vickers, M.D.</p>
      <p class="doctor__title">Hand and Upper Extremity Surgery</p>
    </div>
    <span class="accent-bar"></span>

    <div class="contact-panel">
      <address>38157 North Harbor Blvd<br>Coral Springs, FL 33058</address>
      <p class="contact-line">
        <svg viewBox="0 0 16 16" aria-hidden="true"><path fill="#1fb3e0" d="M3.6 1.5l2.2 2.6-1.3 1.6c.9 2 2.3 3.5 4.2 4.4l1.6-1.3 2.6 2.2-1.2 2.2C6.8 13.2 2.8 9.2 1.5 3.6z"/></svg>
        954-218-4630
      </p>
      <p class="contact-line">
        <svg viewBox="0 0 16 16" aria-hidden="true"><rect x="4" y="1.5" width="8" height="4" fill="none" stroke="#1fb3e0" stroke-width="1.5"/><rect x="1.5" y="5.5" width="13" height="7" rx="1" fill="#1fb3e0"/><rect x="4" y="10" width="8" height="4.5" fill="#fff" stroke="#1fb3e0" stroke-width="1.2"/></svg>
        954-581-2473
      </p>
      <p class="contact-line">
        <svg viewBox="0 0 16 16" aria-hidden="true"><rect x="1.5" y="3.5" width="13" height="9" rx="1" fill="#1fb3e0"/><path d="M2 4.5l6 4.5 6-4.5" fill="none" stroke="#fff" stroke-width="1.3"/></svg>
        info@myrvspine.example
      </p>
    </div>
  </section>

</body>
</html>
```